Brix2Key Header

I want a professional Letterhead for my law firm. I'm attaching the letterhead I currently use in Word and PDF form. I'm also attaching my logo, and an example header that I like.

```html
<!DOCTYPE html>
<html lang="en">
<head>
<meta charset="utf-8">
<title>Brix2Key Letterhead</title>
<link rel="stylesheet" href="https://fonts.googleapis.com/css2?family=Open+Sans:wght@400;700&family=Roboto:wght@400;500&display=swap">
<style>
  :root {
    --backdrop: #dcdcdc;
    --paper: #f7f7f7;
    --ink: #2d2d2f;
    --body-ink: #4d4d4f;
    --brand-blue: #1f6bb5;
    --footer-dark: #333335;
  }
  * { margin: 0; padding: 0; box-sizing: border-box; }
  html, body {
    width: 1153px; height: 1200px; overflow: hidden;
    background: var(--backdrop);
  }
  .letterhead {
    position: absolute; left: 160px; top: 20px;
    width: 832px; height: 1160px;
    background: var(--paper);
    box-shadow: 0 6px 18px rgba(0,0,0,0.12);
    font-family: "Open Sans", Arial, sans-serif;
    color: var(--body-ink);
  }
  .brand {
    position: absolute; left: 75px; top: 100px;
    display: flex; align-items: center; gap: 10px;
  }
  .brand-mark { width: 22px; height: 22px; background: var(--brand-blue); }
  .brand-name {
    font-weight: 700; font-size: 40px; line-height: 1;
    color: var(--ink); letter-spacing: 0.5px;
  }
  .contact {
    position: absolute; right: 76px; top: 82px;
    font-family: "Roboto", Arial, sans-serif;
    font-size: 10px; line-height: 13.5px;
    color: var(--ink); text-align: right;
  }
  .contact-lines { margin-top: 2px; display: inline-block; text-align: left; }
  .contact-line { display: flex; align-items: center; gap: 4px; line-height: 14.3px; }
  .contact-line svg { width: 9px; height: 9px; fill: var(--brand-blue); flex: none; }
  .letter-body {
    position: absolute; left: 75px; top: 300px; width: 681px;
    font-size: 14.9px; line-height: 22.3px;
  }
  .letter-body p { margin-bottom: 22.3px; text-align: justify; }
  .salutation, .closing { text-align: left !important; }
  .signature {
    position: absolute; left: 75px; top: 886px; width: 98px; height: 95px;
    background: linear-gradient(135deg, rgba(40,40,40,0.08), rgba(40,40,40,0.18));
  }
  .footer-stripe {
    position: absolute; left: 0; top: 1125px; width: 100%; height: 7px;
    background: var(--brand-blue);
  }
  .footer-band {
    position: absolute; left: 0; top: 1137px; width: 100%; height: 23px;
    background: var(--footer-dark);
  }
</style>
</head>
<body>
  <div class="letterhead">
    <div class="brand">
      <span class="brand-mark"></span>
      <span class="brand-name">BRIX2KEY</span>
    </div>

    <div class="contact">
      <div>DAMIAN R. CALLOWAY III, ATTORNEY AT LAW, PLLC</div>
      <div>2450 HARWOOD STREET SUITE</div>
      <div>200 AUSTIN, TEXAS 78701</div>
      <div class="contact-lines">
        <div class="contact-line">
          <svg viewBox="0 0 10 10"><path d="M1 4 Q5 0 9 4 L8 5 L6.5 4 L6.5 3.2 Q5 2.7 3.5 3.2 L3.5 4 L2 5 Z M2.5 6 H7.5 V9 H2.5 Z"/></svg>
          (877) 555-0142
        </div>
        <div class="contact-line">
          <svg viewBox="0 0 10 10"><path d="M3 1 H7 V3 H3 Z M1 3.5 H9 V7 H7.5 V9 H2.5 V7 H1 Z"/></svg>
          (469) 555-0187
        </div>
        <div class="contact-line">
          <svg viewBox="0 0 10 10"><path d="M1 2.5 H9 V8 H1 Z M1.5 3 L5 5.6 L8.5 3" stroke="#f7f7f7" stroke-width="0.8"/></svg>
          KEY@BRIX2KEY.NET
        </div>
        <div class="contact-line">
          <svg viewBox="0 0 10 10"><circle cx="5" cy="5" r="4.3"/><path d="M3 3 Q4.5 2.5 5 4 Q4 5.5 3 5 Z M6 6 Q7.5 5.5 7.5 7 Q6.5 8 6 7 Z" fill="#f7f7f7"/></svg>
          WWW.BRIX2KEY.COM
        </div>
      </div>
    </div>

    <div class="letter-body">
      <p class="salutation">Dear customer,</p>
      <p>Lorem ipsum dolor sit amet, consectetur adipisicing elit, sed do eiusmod tempor incididunt ut labore et dolore magna aliqua. Ut enim ad minim veniam, quis nostrud exercitation ullamco laboris nisi ut aliquip ex ea commodo consequat. Duis aute irure dolor in reprehenderit in voluptate velit esse cillum dolore eu fugiat nulla pariatur. Excepteur sint occaecat cupidatat non proident, sunt in culpa qui officia deserunt mollit anim id est laborum.</p>
      <p>Lorem ipsum dolor sit amet, consectetur adipisicing elit, sed do eiusmod tempor incididunt ut labore et dolore magna aliqua. Ut enim ad minim veniam, quis nostrud exercitation ullamco laboris nisi ut aliquip ex ea commodo consequat. Duis aute irure dolor in reprehenderit in voluptate velit esse cillum dolore eu fugiat nulla pariatur. Excepteur sint occaecat cupidatat non proident, sunt in culpa qui officia deserunt mollit anim id est laborum.</p>
      <p>Lorem ipsum dolor sit amet, consectetur adipisicing elit, sed do eiusmod tempor incididunt ut labore et dolore magna aliqua. Ut enim ad minim veniam, quis nostrud exercitation ullamco laboris nisi ut aliquip ex ea commodo consequat. Duis aute irure dolor in reprehenderit in voluptate velit esse cillum dolore eu fugiat nulla pariatur. Excepteur sint occaecat cupidatat non proident, sunt in culpa qui officia deserunt mollit anim id est laborum.</p>
      <p>Lorem ipsum dolor sit amet, consectetur adipisicing elit, sed do eiusmod tempor incididunt ut labore et dolore magna aliqua. Ut enim ad minim veniam, quis nostrud exercitation ullamco laboris nisi ut aliquip ex ea commodo consequat. Duis aute irure dolor in reprehenderit.</p>
      <p class="closing">Yours Sincerely,</p>
    </div>

    <div class="signature" role="img" aria-label="Handwritten signature of the attorney"></div>

    <div class="footer-stripe"></div>
    <div class="footer-band"></div>
  </div>
</body>
</html>
```